11"x17" Brochure on Concept Showroom

We need a designer to take our artwork, graphics, and text to create a 11"x17" bi-fold brochure (printed front and back). The designer should take liberties to add in their own artwork, graphics, and stock photos to support the presentation of the story as professionally as possible.

I've included a lot of artwork, not all is to be used. Only provided so that you have a selection to choose from.

Page 1 (Outside Front) - Graphics, Logo, Tag Line
Page 2 (Inside Left) - Center Graphics, Descriptive Text
Page 3 (Inside Right) - Tier Levels
Page 4 (Outside Back) - Location and contact information

In addition to the artwork the following files are attached:
1. A PDF document with textual information and concept markup
2. An Excel spreadsheet with the service tier levels
3. Our Logo
4. Design/Print parameters (Link below: https://www.filquarry.net/s/k7tr2wplx8mzqe4/90357218640288X17-SHEET.jpg?dl=0)

Feel free to message me and ask questions. This is a fast track project and I need to send to printing by Thursday at 5pm EST.

YOU ARE THE DESIGN PROFESSIONAL - Please use my concept only to set the idea of what is needed. Feel free to take liberties in design.

Target Market(s)

Manufacturers of security electronics

Industry/Entity Type

Security

Font styles to use
Serif

Requirements
Must have
• Concept designs, Tier levels of service, Location Information, simplistic look. The service tier levels will be Bronze, Silver, Gold, Platinum. Where in the excel spreadsheet you see an "x" it should have a green checkmark indicating its included.
Nice to have
• On page 4 a picture of the overall concept center with lines pointing to/calling out the areas in the concept center.
Should not have
• Too many photos/graphics, crowded pages

```html
<!DOCTYPE html>
<html lang="en">
<head>
<meta charset="utf-8">
<title>Your Showroom in New York City – Vantage Consulting</title>
<link rel="stylesheet" href="https://fonts.googleapis.com/css2?family=Mulish:ital,wght@0,400;0,700;1,700;1,800&display=swap">
<style>
  :root {
    --bg: #3b3c3e;
    --bg-deep: #323335;
    --band: #1f2022;
    --accent: #2aa9e0;
    --text: #f2f2f2;
  }
  * { margin: 0; padding: 0; box-sizing: border-box; }
  html, body { width: 927px; height: 1200px; overflow: hidden; }
  body { font-family: "Mulish", "Helvetica Neue", Arial, sans-serif; }

  .flyer {
    position: relative;
    width: 927px;
    height: 1200px;
    background: radial-gradient(ellipse at 40% 35%, var(--bg) 0%, var(--bg-deep) 100%);
    overflow: hidden;
  }

  .headline {
    position: absolute;
    left: 284px;
    top: 338px;
    font-size: 66px;
    font-weight: 800;
    font-style: italic;
    color: var(--accent);
    letter-spacing: -0.5px;
    line-height: 1;
  }

  .offer-list {
    position: absolute;
    left: 262px;
    top: 466px;
    list-style: none;
  }
  .offer-list li {
    position: relative;
    padding-left: 27px;
    height: 43.6px;
    font-size: 22px;
    font-weight: 400;
    color: var(--text);
    line-height: 28px;
  }
  .offer-list li::before {
    content: "";
    position: absolute;
    left: 0;
    top: 9px;
    width: 10px;
    height: 9px;
    background: var(--accent);
    clip-path: polygon(100% 0, 100% 100%, 0 100%);
  }

  .location {
    position: absolute;
    left: 290px;
    top: 820px;
    font-size: 37px;
    font-weight: 700;
    font-style: italic;
    color: var(--accent);
  }

  .brand-band {
    position: absolute;
    left: 0;
    bottom: 0;
    width: 100%;
    height: 156px;
    background: var(--band);
  }
  .brand {
    position: absolute;
    right: 62px;
    top: 40px;
    display: flex;
    align-items: center;
    gap: 16px;
  }
  .brand-dot {
    width: 40px;
    height: 40px;
    border-radius: 50%;
    background: var(--accent);
  }
  .brand-name {
    color: var(--text);
    font-weight: 700;
    line-height: 1;
  }
  .brand-name .main { display: block; font-size: 58px; letter-spacing: -1px; }
  .brand-name .sub { display: block; font-size: 14px; letter-spacing: 14px; margin-top: 6px; }
</style>
</head>
<body>
  <main class="flyer">
    <h1 class="headline">your….</h1>

    <ul class="offer-list">
      <li>Address</li>
      <li>Showroom</li>
      <li>Security Operation Center</li>
      <li>Conference Center</li>
      <li>Training Center</li>
      <li>Design Center</li>
      <li>Collaborative Sales Environment</li>
      <li>and Office Space</li>
    </ul>

    <p class="location">in New York City</p>

    <footer class="brand-band">
      <div class="brand">
        <span class="brand-dot"></span>
        <p class="brand-name"><span class="main">vantage</span><span class="sub">CONSULTING</span></p>
      </div>
    </footer>
  </main>
</body>
</html>
```